Wordpress Design Project

I now need a Wordpress theme for my new business.
The business offers consultancy on Information Management, Knowledge Management, Records Management and Document Management.
The winning designer must be able to set up the site for me on my webspace provided by Tallowbrook Hosting, or talk me through how to do this.
I already have a logo designed which you can see by viewing my profile on here. I am happy to send copies of the original artwork to bidders.
I recently sold my interest in a very similar business, and want a website similar to (but not the same as) the previous company (who are now my competition!) This website can be viewed at www.qardvane.com
Categories will be similar, but I would like everything to be as configurable as possible.
I have a strong preference for clean unfussy design.
I want original design please. Please no templates from free to use sites with stock images... no jigsaw pictures!!!!
Love this one... http://www.felquist.tv/
Please get in touch with any questions.
Updates
Project Deadline Extended
Reason: All of these are too generic (brief says no jigsaw puzzle images), or have copied QDV which is the COMPETITION - so I don't want the site to look like theirs
Project Deadline Extended
Reason: Please keep trying people
Business
Business

```html
<!DOCTYPE html>
<html lang="en">
<head>
<meta charset="utf-8">
<title>Harwick Professional Services</title>
<link rel="stylesheet" href="https://fonts.googleapis.com/css2?family=Gelasio:wght@400;700&family=Arimo:wght@400&family=PT+Sans:wght@400;700&display=swap">
<style>
:root{
  --page-bg:#eeeeee;
  --column-bg:#ffffff;
  --navy:#1d3466;
  --link-blue:#2a8fd4;
  --text:#333333;
  --muted:#8a8a8a;
  --hero-band:#8db5d2;
  --frame:#bcd0e3;
  --footer-band:#1f3f84;
  --footer-bar:#e1e1e1;
}
*{margin:0;padding:0;box-sizing:border-box}
html,body{width:1200px;height:956px;overflow:hidden}
body{background:var(--page-bg);font-family:"Arimo",Arial,sans-serif;color:var(--text);position:relative}
.page-column{position:absolute;left:144px;top:0;width:910px;height:956px;background:var(--column-bg);box-shadow:0 0 6px rgba(0,0,0,.12)}
a{color:inherit;text-decoration:none}

/* header */
.brand-name{position:absolute;left:170px;top:46px;font-family:"Gelasio",Georgia,serif;font-weight:700;font-size:27px;line-height:1;color:var(--navy)}
.contact{position:absolute;top:9px;right:172px;display:flex;gap:24px;font-size:14px;color:var(--link-blue);align-items:center}
.contact span{display:flex;align-items:center;gap:8px}
.contact .email{text-decoration:underline}
.main-nav{position:absolute;top:89px;left:0;width:1200px;height:30px;font-family:"Gelasio",Georgia,serif;font-size:13px;color:var(--muted)}
.main-nav a{position:absolute;top:0;padding-top:7px;border-top:2px solid transparent;white-space:nowrap}
.main-nav a.current{color:var(--navy);font-weight:700;border-top-color:var(--navy)}

/* hero */
.hero-band{position:absolute;left:0;top:120px;width:1200px;height:322px;background:var(--hero-band)}
.hero-photo{position:absolute;left:144px;top:120px;width:910px;height:322px;background:linear-gradient(120deg,#c9c9c9 0%,#8f8f8f 35%,#d8d8d8 60%,#6f6f6f 100%)}
.slide-dots{position:absolute;left:976px;top:251px;display:flex;gap:3px}
.slide-dots i{width:7px;height:7px;background:#fff;display:block}
.slide-dots i.active{background:#5aaee6}
.hero-caption{position:absolute;left:522px;top:265px;width:507px;height:177px;background:rgba(246,246,246,.94);padding:14px 21px}
.hero-caption h1{font-family:"Gelasio",Georgia,serif;font-weight:700;font-size:24px;color:var(--navy);line-height:1.2}
.hero-caption p{font-family:"PT Sans",sans-serif;font-size:14.3px;line-height:18px;color:#222;margin-top:12px}
.button{position:absolute;left:24px;top:124px;width:99px;height:33px;border-radius:3px;background:linear-gradient(#4a87c8,#1f4d90);border:1px solid #173d74;color:#0c1f3e;font-family:"PT Sans",sans-serif;font-weight:700;font-size:12px;display:flex;align-items:center;justify-content:center;box-shadow:0 3px 4px rgba(0,0,0,.25)}

/* services */
.service{position:absolute;width:420px}
.service .thumb{position:absolute;left:0;top:0;width:144px;height:180px;border:6px solid var(--frame)}
.service .body{position:absolute;left:162px;top:0;width:258px}
.service h2{font-family:"Gelasio",Georgia,serif;font-weight:700;font-size:18.5px;line-height:21px;color:var(--navy)}
.service p{font-size:12px;line-height:18px;margin-top:6px;color:#333}
.read-more{display:flex;align-items:center;gap:5px;margin-top:8px;font-size:12px;color:var(--link-blue)}
.read-more span{text-decoration:underline}
.s1{left:168px;top:476px}.s2{left:622px;top:476px}.s3{left:168px;top:698px}.s4{left:622px;top:698px}
.thumb-hands{background:linear-gradient(135deg,#f5f5f5,#d7d2cc 60%,#b9b3aa)}
.thumb-head{background:radial-gradient(circle at 50% 35%,#7fc6ff,#1a4fa0 45%,#02091c 90%)}
.thumb-pins{background:linear-gradient(135deg,#e7f0f8,#a8c4dd 55%,#2a4fa5)}
.thumb-files{background:linear-gradient(120deg,#dfe9f4,#6f9acb 50%,#1c3f80)}

/* footer */
.footer-band{position:absolute;left:0;top:916px;width:1200px;height:40px;background:var(--footer-band)}
.footer-bar{position:absolute;left:144px;top:916px;width:910px;height:40px;background:var(--footer-bar);display:flex;align-items:center;justify-content:space-between;padding:0 25px 0 24px;font-size:12px;color:#888}
.footer-nav a{color:#888}
.footer-nav a.current{color:#333}
.footer-nav .sep{margin:0 15px;color:#999}
</style>
</head>
<body>
<div class="page-column"></div>

<header>
  <div class="brand-name">Harwick Professional Services</div>
  <div class="contact">
    <span>
      <svg width="12" height="18" viewBox="0 0 12 18"><rect x="1" y="0" width="10" height="18" rx="2" fill="#555"/><rect x="3" y="2" width="6" height="6" fill="#ddd"/></svg>
      0161-555-0187
    </span>
    <span>
      <svg width="17" height="12" viewBox="0 0 17 12"><rect width="17" height="12" fill="#555"/><path d="M0 0 8.5 7 17 0" stroke="#ddd" stroke-width="1.5" fill="none"/></svg>
      <a class="email" href="#">hello@harwick-ps.example</a>
    </span>
  </div>
  <nav class="main-nav">
    <a class="current" href="#" style="left:609px">Home</a>
    <a href="#" style="left:673px">About Us</a>
    <a href="#" style="left:754px">Services</a>
    <a href="#" style="left:829px">Technology</a>
    <a href="#" style="left:924px">News</a>
    <a href="#" style="left:983px">Contact</a>
  </nav>
</header>

<section class="hero">
  <div class="hero-band"></div>
  <div class="hero-photo" role="img" aria-label="Black and white photo of hands working over technical plans on a desk beside a glass of water"></div>
  <div class="slide-dots"><i class="active"></i><i></i><i></i><i></i><i></i></div>
  <div class="hero-caption">
    <h1>Lorem ipsum dolor sit amet</h1>
    <p>Lorem ipsum dolor sit amet, consectetur adipiscing elit. Nam purus nulla, cursus non convallis ut, egestas at quam. Quisque vitae neque et lacus fe rmentum lobortis non non ligula.</p>
    <a class="button" href="#">Read More</a>
  </div>
</section>

<main>
  <article class="service s1">
    <div class="thumb thumb-hands" role="img" aria-label="Photo of hands reviewing paper documents"></div>
    <div class="body">
      <h2>Consultancy on<br>Information Managment</h2>
      <p>Lorem ipsum dolor sit amet, consectetur adipiscing elit. Nam purus nulla, cursus non convallis ut, egestas at quam. Quisque vitae neque et lacus fermentum lobortis non non ligula. Donec vitae arcu risus, eu pellen-tesque massa.</p>
      <a class="read-more" href="#"><svg width="13" height="8" viewBox="0 0 13 8"><path d="M0 4h11M8 1l3 3-3 3" stroke="#1d3466" stroke-width="1.5" fill="none"/></svg><span>Read More</span></a>
    </div>
  </article>
  <article class="service s2">
    <div class="thumb thumb-head" role="img" aria-label="Illustration of glowing blue data streams over a head silhouette"></div>
    <div class="body">
      <h2>Knowledge Management</h2>
      <p>Lorem ipsum dolor sit amet, consectetur adipiscing elit. Nam purus nulla, cursus non convallis ut, egestas at quam. Quisque vitae neque et lacus fermentum lobortis non non ligula. Donec vitae arcu risus, eu pellen-tesque massa.</p>
      <a class="read-more" href="#"><svg width="13" height="8" viewBox="0 0 13 8"><path d="M0 4h11M8 1l3 3-3 3" stroke="#1d3466" stroke-width="1.5" fill="none"/></svg><span>Read More</span></a>
    </div>
  </article>
  <article class="service s3">
    <div class="thumb thumb-pins" role="img" aria-label="Photo of blue push pins on a light blue surface"></div>
    <div class="body">
      <h2>Records Management</h2>
      <p>Lorem ipsum dolor sit amet, consectetur adipiscing elit. Nam purus nulla, cursus non convallis ut, egestas at quam. Quisque vitae neque et lacus fermentum lobortis non non ligula. Donec vitae arcu risus, eu pellen-tesque massa.</p>
      <a class="read-more" href="#"><svg width="13" height="8" viewBox="0 0 13 8"><path d="M0 4h11M8 1l3 3-3 3" stroke="#1d3466" stroke-width="1.5" fill="none"/></svg><span>Read More</span></a>
    </div>
  </article>
  <article class="service s4">
    <div class="thumb thumb-files" role="img" aria-label="Illustration of file folders coming out of a computer screen"></div>
    <div class="body">
      <h2>Document Management</h2>
      <p>Lorem ipsum dolor sit amet, consectetur adipiscing elit. Nam purus nulla, cursus non convallis ut, egestas at quam. Quisque vitae neque et lacus fermentum lobortis non non ligula. Donec vitae arcu risus, eu pellen-tesque massa.</p>
      <a class="read-more" href="#"><svg width="13" height="8" viewBox="0 0 13 8"><path d="M0 4h11M8 1l3 3-3 3" stroke="#1d3466" stroke-width="1.5" fill="none"/></svg><span>Read More</span></a>
    </div>
  </article>
</main>

<footer>
  <div class="footer-band"></div>
  <div class="footer-bar">
    <nav class="footer-nav">
      <a class="current" href="#">Home</a><span class="sep">|</span><a href="#">About Us</a><span class="sep">|</span><a href="#">Services</a><span class="sep">|</span><a href="#">Technology</a><span class="sep">|</span><a href="#">News</a><span class="sep">|</span><a href="#">Contact</a>
    </nav>
    <div class="copyright">Copyright ©2012 Harwick Professional Services</div>
  </div>
</footer>
</body>
</html>
```